CD Cover Design Project

Something very cool but simple. I need front, back, sleeve and disc. Disc I would like to have the old piano on from the pictures.

Target Market(s)

Fans, Music industry

Requirements
Must have
• Must have disc with piano keys on it. Please use the back photo for the piano keys. Thanks

All the text

Back:
Moonlit

1. Holdin' On

2. He Rides Slow

3. Late To Leave

4. Road We Wandered Down (Acoustic)

disc:
Corliss Vantree

Moonlit

Holdin' On

He Rides Slow

Late To Leave

Road We Wandered Down (Acoustic)

Left Side:

Short Bio

A big thanks to my Mom, Sister and Dad. Also to Dusty Crandall, Gordon Pelk (mixes), Dale Morrow, Winona P. Melody Garrick, Ray Dunmore, Loretta Baskin, Glen Ostrova, Wade Pruitt, Otis Feldhammer, Curtis Ambley,Hal Quimbly, Darla Wenrich, Lyle Ferraday, and all my Backer Tunes supporters. I couldn't have done it without you.

Holdin' On written by Garrick and Vantree. He Rides Slow written by Vantree and Oakhurst, Late To Leave written by Vantree
and Road We Wandered Down written by Vantree and Gantry.

Right side:photo
Nice to have
• I would like to use the middle shot with the red dress if possible but not sure it's large enough. If not please use the other middle shot with the colors shirt and the mandolin. Thanks
Should not have
• Not too dark. Not to blocky.. Inclosed is something done this week that I don't like. Bad fonts and no graphics.

```html
<!DOCTYPE html>
<html lang="en">
<head>
<meta charset="utf-8">
<title>Corliss Vantree – Moonlit – 4-Panel Digipak</title>
<link rel="stylesheet" href="https://fonts.googleapis.com/css2?family=Marcellus+SC&family=Open+Sans:wght@400;700&display=swap">
<style>
:root{
  --paper:#ffffff;
  --guide-blue:#9ab8dc;
  --safe-green:#9fdcc0;
  --bleed-red:#d9303a;
  --tray-red:#c01a22;
  --tray-red-dark:#9a1118;
  --spine-red:#6b1a22;
  --label-gray:#8a8a8a;
  --ink-white:#ffffff;
  --label-blue:#2f4aa0;
}
*{box-sizing:border-box;margin:0;padding:0}
html,body{width:1200px;height:1074px;overflow:hidden;background:var(--paper)}
body{position:relative;font-family:"Open Sans",Arial,sans-serif}
.panel{position:absolute;overflow:hidden}
.photo{position:absolute;inset:0}
.safe{position:absolute;border:1px solid var(--safe-green);pointer-events:none}
.title{font-family:"Marcellus SC",serif;font-weight:400;color:var(--ink-white);text-align:right;line-height:1}
.title .name,.title .album{display:block}

/* inside left */
.inside-left{left:70px;top:36px;width:518px;height:464px;border:1px solid var(--bleed-red)}
.inside-left .photo{background:linear-gradient(90deg,#6e2a26 0%,#5a2320 22%,#3a1f1b 38%,#2c2320 48%,#5e5750 66%,#8d857c 82%,#a49b91 100%)}
.inside-left .title{position:absolute;right:45px;top:30px}
.inside-left .name{font-size:20px;letter-spacing:.4px}
.inside-left .album{font-size:14px;margin-top:2px}
.bio{position:absolute;left:227px;top:88px;width:247px;color:var(--ink-white);font-size:7.7px;line-height:11px;text-align:justify}
.bio p{margin-bottom:11px}

/* tray */
.inside-right{left:612px;top:36px;width:518px;height:464px;border:1px solid var(--bleed-red);background:var(--tray-red)}
.disc{position:absolute;left:27px;top:9px;width:448px;height:448px;border-radius:50%;overflow:hidden}
.disc .photo{background:linear-gradient(60deg,#e6dccb 0%,#cfc3ae 18%,#2a211c 30%,#4b3d33 48%,#6f6257 64%,#3a2f28 80%,#1f1915 100%)}
.disc .title{position:absolute;right:170px;top:100px}
.disc .name{font-size:20px}
.disc .album{font-size:14px;margin-top:2px}
.disc-tracks{position:absolute;left:98px;top:263px;list-style:none;color:var(--ink-white);font-size:9px}
.disc-tracks li{height:25.5px}

/* back cover */
.back-cover{left:70px;top:538px;width:518px;height:464px;border:1px solid var(--bleed-red)}
.back-cover .photo{background:linear-gradient(180deg,rgba(0,0,0,0) 55%,rgba(196,110,170,.55) 78%,rgba(200,190,70,.55) 100%),linear-gradient(90deg,#6f6a3f 0%,#9c8f6c 22%,#c9b99c 45%,#d6c8ae 62%,#bba78c 82%,#9d8a70 100%)}
.back-cover .title{position:absolute;left:43px;top:149px}
.back-cover .name{font-size:19px}
.back-cover .album{font-size:13px;margin-top:1px}
.back-tracks{position:absolute;left:44px;top:197px;list-style:none;color:var(--ink-white);font-size:9.5px}
.back-tracks li{height:26.5px}
.label-name{position:absolute;left:326px;top:430px;width:172px;text-align:center;color:var(--label-blue);font-size:10px;font-weight:700;letter-spacing:.3px}

/* spine */
.spine{left:588px;top:538px;width:24px;height:464px;background:var(--spine-red)}
.spine-text{position:absolute;left:23px;top:108px;transform-origin:0 0;transform:rotate(90deg);white-space:nowrap;font-family:"Marcellus SC",serif;color:var(--ink-white);font-size:16px;line-height:24px}
.spine-text .album{margin-left:26px;font-size:12px}

/* front cover */
.front-cover{left:612px;top:538px;width:518px;height:464px;border:1px solid var(--bleed-red)}
.front-cover .photo{background:linear-gradient(180deg,rgba(0,0,0,0) 70%,#e9dc8c 88%,#f1e6a4 100%),linear-gradient(90deg,#3a2a20 0%,#6a4634 14%,#b88a70 30%,#a6765e 44%,#4a3426 60%,#2e231d 80%,#3a2c24 100%)}
.front-cover .title{position:absolute;right:35px;top:121px}
.front-cover .name{font-size:23px;letter-spacing:.4px}
.front-cover .album{font-size:15px;margin-top:3px}

/* template marks */
.guides{position:absolute;inset:0;pointer-events:none}
.tray-note{position:absolute;left:1143px;top:130px;writing-mode:vertical-rl;font-weight:700;font-size:26px;color:var(--label-gray)}
.cover-label{position:absolute;top:1012px;font-weight:700;font-size:29px;color:var(--label-gray)}
.cover-label.back{left:226px}
.cover-label.front{left:757px}
.template-tag{position:absolute;left:77px;top:1020px;width:118px;height:48px;border:1px solid #333;display:flex;align-items:center;padding-left:6px;gap:8px;font-size:6px;line-height:7px;text-align:center;color:#222}
.template-tag .mark{width:22px;height:22px;background:#2aa7d8;flex:none}
.template-tag strong{display:block;font-size:12px;line-height:13px}
.paste-note{position:absolute;left:198px;top:1060px;font-size:6px;color:#333}
</style>
</head>
<body>

<section class="panel inside-left">
  <div class="photo" role="img" aria-label="Photo of the singer in a red lace dress seated at an old upright piano"></div>
  <div class="safe" style="left:11px;top:6px;right:14px;bottom:11px"></div>
  <h2 class="title"><span class="name">CORLISS VANTREE</span><span class="album">MOONLIT</span></h2>
  <div class="bio">
    <p>The Virginia-Born performer had a successful music career Off Broadway and in TV and Film before launching her Country career after a chance encounter with a songwriter while shooting the CRN reality show "Spotlight Showdown". Corliss has been blessed to travel around the world for music.</p>
    <p>"Being from VA I've always loved Country music, especially our native Mabel Dorsey, and sang some Pop and Country but went the classical direction after High School. Spotlight Showdown brought me back to my roots but I was given the tools to know how to really sing. I wouldn't trade that for anything!"</p>
    <p>"Playing shows around the Country can sometimes be stressful, lack of food, rest, etc... But one night in Kansas it was all put into perspective. A man came up to me after the show and said "this was the worst week of my life and you made it better." That is a blessing that I will never forget, being able to make someone happy through song." I hope you enjoy the songs!</p>
    <p>A big thanks to my Mom, Sister and Dad. Also to Dusty Crandall, Gordon Pelk (mixes), Dale Morrow, Winona P. Melody Garrick, Ray Dunmore, Loretta Baskin, Glen Ostrova, Wade Pruitt, Otis Feldhammer, Curtis Ambley, Hal Quimbly, Darla Wenrich, Lyle Ferraday, and all my Backer Tunes supporters.</p>
    <p>I couldn't have done it without you.</p>
    <p>Holdin' On written by Garrick and Vantree. He Rides Slow written by Vantree and Oakhurst. Late To Leave written by Vantree and Road We Wandered Down written by Vantree and Gantry.</p>
  </div>
</section>

<section class="panel inside-right">
  <div class="disc">
    <div class="photo" role="img" aria-label="Close-up photo of old upright piano keys and wooden key frame, a hand playing"></div>
    <h2 class="title"><span class="name">CORLISS VANTREE</span><span class="album">MOONLIT</span></h2>
    <ol class="disc-tracks">
      <li>1. Holdin' On</li>
      <li>2. He Rides Slow</li>
      <li>3. Late To Leave</li>
      <li>4. Road We Wandered Down (Acoustic)</li>
    </ol>
  </div>
  <svg class="guides" viewBox="0 0 518 464" width="518" height="464" aria-hidden="true">
    <g fill="none" stroke="var(--safe-green)" stroke-width="1">
      <circle cx="251" cy="233" r="226"/>
      <path d="M60 70 A30 30 0 1 1 100 28 M400 28 A30 30 0 1 1 440 70 M60 394 A30 30 0 1 0 100 436 M400 436 A30 30 0 1 0 440 394"/>
      <path d="M226 196 A44 44 0 0 0 226 268 M276 196 A44 44 0 0 1 276 268"/>
    </g>
    <circle cx="251" cy="232" r="23" fill="var(--tray-red)" stroke="#ffffff" stroke-width="1"/>
    <path d="M251 209 V255 M228 232 H274" stroke="#ffffff" stroke-width="1"/>
  </svg>
</section>

<section class="panel back-cover">
  <div class="photo" role="img" aria-label="Photo of the singer in a colourful off-shoulder top in a sunny courtyard, mandolin at lower left"></div>
  <div class="safe" style="left:11px;top:11px;right:11px;bottom:11px"></div>
  <h2 class="title"><span class="name">CORLISS VANTREE</span><span class="album">MOONLIT</span></h2>
  <ol class="back-tracks">
    <li>1. Holdin' On</li>
    <li>2. He Rides Slow</li>
    <li>3. Late To Leave</li>
    <li>4. Road We Wandered Down (Acoustic)</li>
  </ol>
  <div class="label-name">NORTHSTAR HOLLOW RECORDS</div>
</section>

<section class="panel spine">
  <div class="spine-text"><span class="name">CORLISS VANTREE</span><span class="album">MOONLIT</span></div>
</section>

<section class="panel front-cover">
  <div class="photo" role="img" aria-label="Portrait photo of the singer with long dark hair in a yellow lace top"></div>
  <div class="safe" style="left:11px;top:11px;right:11px;bottom:11px"></div>
  <h1 class="title"><span class="name">CORLISS VANTREE</span><span class="album">MOONLIT</span></h1>
</section>

<svg class="guides" viewBox="0 0 1200 1074" width="1200" height="1074" aria-hidden="true">
  <g fill="none" stroke="var(--guide-blue)" stroke-width="1">
    <rect x="64" y="36" width="533" height="477"/>
    <rect x="603" y="36" width="533" height="477"/>
    <rect x="64" y="524" width="1072" height="492"/>
    <path d="M35 36 H64 M1136 36 H1165 M0 500 H64 M1136 500 H1200 M0 570 H64 M1136 570 H1200 M35 1002 H64 M1136 1002 H1165"/>
    <path d="M588 1016 V1036 M612 1016 V1036 M70 1016 V1036 M1130 1016 V1036"/>
    <path d="M64 640 H75 M64 706 H75"/>
  </g>
</svg>

<div class="tray-note">TRAY GOES HERE</div>
<div class="cover-label back">BACK COVER</div>
<div class="cover-label front">FRONT COVER</div>

<div class="template-tag">
  <span class="mark"></span>
  <div><strong>4PAN1T</strong>4-Panel Digipak w/<br>1 Tray<br>PDF<br>03/23/11 CJM</div>
</div>
<div class="paste-note">PASTE PKG TAG HERE</div>

</body>
</html>
```